Wellness Wordpress Blog Redesign

I am looking to redesign by wordpress blog - www.MarenCrowleyActive.com. I would like to have a more personalized feel that resonates with my brand of Renewed Balance through fitness, nutrition, self care and self love. I'd like capabilities to do the following:

Ideally, I'd like to have the home page feature not only my latest blog posts or videos, but to also include a place to click to learn more about other facets of my business.

Ideally, I'd love to have a page layout of:

Home - main page to host key features of the brand & latest blog posts
About - Place to learn more about me and my brand
Blog -
Fitness - Host some videos and fitness tips and links to resources
Nutrition - Host some videos and recipes and links to resources
Self Care - Host some videos and self care tips and links to resources
Shop - Host a video (that can be changed of the product of the month) and links to other resources

Number of Pages Required

5+ page

Font styles to use
Serif
Decorative

Colors
85acd3
0393ce
00a990
6b449b
a64599
b8a6cd

Requirements
Must have
• Home - main page to host key features of the brand & latest blog posts
• About - Place to learn more about me and my brand
• Blog -
• Fitness - Host some videos and fitness tips and links to resources
• Nutrition - Host some videos and recipes and links to resources
• Self Care - Host some videos and self care tips and links to resources
• Shop - Host a video (that can be changed of the product of the month) and links to other resources
• Video / Mutlimedia capabilities
Nice to have
• Option to have a calendar of events widgets for people to sign up for events that I'm hosting

```html
<!DOCTYPE html>
<html lang="en">
<head>
<meta charset="utf-8">
<title>Maren Crowley — Home</title>
<link rel="stylesheet" href="https://fonts.googleapis.com/css2?family=Roboto:wght@400;500;700&family=Kaushan+Script&family=Saira+Condensed:wght@700&family=Barlow:wght@400&display=swap">
<style>
  :root {
    --purple: #6b449b;
    --teal: #00a990;
    --cyan: #0393ce;
    --ink: #111111;
    --black: #000000;
    --white: #ffffff;
    --panel: rgba(0,0,0,0.72);
    --cover-green: #0f6b26;
  }
  * { box-sizing: border-box; margin: 0; padding: 0; }
  html, body { width: 1171px; height: 1200px; overflow: hidden; background: var(--white); }
  body { position: relative; font-family: "Roboto", Arial, sans-serif; color: var(--ink); }

  .site-header { position: absolute; left: 0; top: 0; width: 1171px; height: 122px; background: var(--white); border-bottom: 1px solid #ddd; }
  .brand { position: absolute; left: 46px; top: 36px; font-family: "Roboto", sans-serif; font-weight: 500; font-size: 40px; color: var(--purple); letter-spacing: 0.5px; }
  .main-nav a { position: absolute; top: 45px; font-size: 19px; color: var(--ink); text-decoration: none; }
  .main-nav a.is-current::after { content: ""; position: absolute; left: 0; right: 0; bottom: -7px; height: 3px; background: var(--purple); }

  .hero { position: absolute; left: 0; top: 122px; width: 1171px; height: 579px; }
  .hero-photo { position: absolute; inset: 0; background: radial-gradient(ellipse at 35% 55%, #6b5a44 0%, #3d3128 55%, #241c17 100%); }
  .hero-panel { position: absolute; left: 630px; top: 136px; width: 541px; height: 301px; background: var(--panel); }
  .hero-title { position: absolute; left: 20px; top: 22px; width: 510px; font-family: "Kaushan Script", cursive; font-weight: 400; font-size: 60px; line-height: 80px; color: var(--white); text-align: center; white-space: nowrap; }
  .hero-text { position: absolute; left: 62px; top: 198px; width: 470px; font-size: 18px; line-height: 23px; color: var(--white); white-space: nowrap; }
  .read-more { position: absolute; right: 50px; top: 256px; font-size: 18px; font-weight: 700; color: var(--white); text-decoration: none; display: flex; align-items: center; gap: 8px; }
  .hero-strip { position: absolute; left: 630px; top: 437px; width: 378px; height: 142px; background: var(--black); color: var(--white); }
  .strip-item { position: absolute; top: 36px; }
  .strip-num { font-size: 19px; font-weight: 400; }
  .strip-label { margin-top: 16px; font-size: 17px; font-weight: 700; }
  .strip-sub { font-size: 11px; color: #bbb; }
  .strip-photo { position: absolute; left: 1008px; top: 437px; width: 163px; height: 142px; background: linear-gradient(135deg, #2a8fa3, #1c7489); }

  .guide { position: absolute; left: 0; top: 701px; width: 1171px; height: 499px; border: 1px solid #999; border-left: none; }
  .cover { position: absolute; left: 0; top: 0; width: 311px; height: 499px; }
  .cover-tile { position: absolute; }
  .cover-band { position: absolute; left: 0; top: 189px; width: 311px; height: 120px; background: var(--cover-green); color: var(--white); text-align: center; }
  .cover-band .script { font-family: "Kaushan Script", cursive; font-size: 48px; line-height: 56px; margin-top: 12px; }
  .cover-band .caps { font-family: "Roboto", sans-serif; font-weight: 700; font-size: 31px; line-height: 32px; letter-spacing: 1px; }
  .cover-credit { position: absolute; left: 30px; top: 449px; width: 246px; height: 36px; background: var(--white); font-size: 11px; letter-spacing: 3px; color: #333; display: flex; align-items: center; justify-content: center; }
  .guide-title { position: absolute; left: 451px; top: 52px; font-family: "Kaushan Script", cursive; font-weight: 400; font-size: 72px; color: var(--teal); white-space: nowrap; }
  .guide-sub { position: absolute; left: 427px; top: 150px; font-family: "Saira Condensed", sans-serif; font-weight: 700; font-size: 29px; line-height: 34px; font-variant: small-caps; letter-spacing: 1.4px; color: var(--ink); white-space: nowrap; }
  .guide-body { position: absolute; left: 427px; top: 221px; width: 740px; font-family: "Barlow", sans-serif; font-size: 13.6px; line-height: 17.8px; color: #222; }
</style>
</head>
<body>
  <header class="site-header">
    <div class="brand">Maren Crowley</div>
    <nav class="main-nav">
      <a class="is-current" href="#" style="left:442px">Home</a>
      <a href="#" style="left:548px">About</a>
      <a href="#" style="left:647px">Blog</a>
      <a href="#" style="left:721px">Fitness</a>
      <a href="#" style="left:829px">Nutrition</a>
      <a href="#" style="left:939px">Self Care</a>
      <a href="#" style="left:1064px">Shop</a>
    </nav>
  </header>

  <section class="hero">
    <div class="hero-photo" role="img" aria-label="Photo of hands slicing vegetables on a wooden cutting board"></div>
    <div class="hero-panel">
      <h1 class="hero-title">3 Tips to Eat<br>Clean This Year</h1>
      <p class="hero-text">Lorem Isum lorem Lorem Isum lorem Lorem Isum lo<br>Lorem Isum lorem Lorem Isum lorem Lorem</p>
      <a class="read-more" href="#">Read more
        <svg width="10" height="14" viewBox="0 0 10 14"><path d="M2 1 L8 7 L2 13" fill="none" stroke="#0393ce" stroke-width="3"/></svg>
      </a>
    </div>
    <div class="hero-strip">
      <div class="strip-item" style="left:36px">
        <div class="strip-num">01</div>
        <div class="strip-label">NEXT</div>
        <div class="strip-sub">loremlpsum det jervis</div>
      </div>
      <div class="strip-item" style="left:206px">
        <div class="strip-num">02</div>
        <div class="strip-label">CATALOGUE</div>
        <div class="strip-sub">loremlpsum det jervis</div>
      </div>
    </div>
    <div class="strip-photo" role="img" aria-label="Photo of a meal prep container with broccoli and chicken on a teal surface"></div>
  </section>

  <section class="guide">
    <div class="cover">
      <div class="cover-tile" style="left:0;top:0;width:155px;height:189px;background:linear-gradient(135deg,#8a9a6a,#c9b79a)" role="img" aria-label="Photo of a chicken salad"></div>
      <div class="cover-tile" style="left:156px;top:0;width:155px;height:189px;background:linear-gradient(160deg,#c0281c,#6fae3a)" role="img" aria-label="Photo of red and green tomatoes"></div>
      <div class="cover-tile" style="left:0;top:309px;width:155px;height:190px;background:linear-gradient(135deg,#4a3428,#7d8a5a)" role="img" aria-label="Photo of grilled fish with green beans"></div>
      <div class="cover-tile" style="left:156px;top:309px;width:155px;height:190px;background:linear-gradient(135deg,#e98a1c,#8b3a20)" role="img" aria-label="Photo of oranges and pears in a bowl"></div>
      <div class="cover-band">
        <div class="script">Clean Eating</div>
        <div class="caps">GUIDE</div>
      </div>
      <div class="cover-credit">CREATED BY MAREN CROWLEY</div>
    </div>
    <h2 class="guide-title">Clean Eating Guide</h2>
    <h3 class="guide-sub">Stop Dieting &amp; Start Losing Weight with Clean Eating</h3>
    <p class="guide-body">Many people fail to stay on track, because they fail to plan. Before the challenge begins, pull out your calendar and get a better idea of what you have going on this week. If your mornings are rushed, ensure that you have a healthy breakfast ready to grab and go in the morning to eat at work, like overnight oats. If you have a work lunch, research the restaurant to find a healthy option or ask the person coordinating the lunch to order you a salad. If you're going to be busy at night, pack a dinner with you or meal prep some dinners (or any other meals) so that way you will have a healthy meal in your fridge. Here are some meal prep tips for you.</p>
  </section>
</body>
</html>
```